I'm Throwing My 4th Annual Grand Clash Watch Party. This is a classy, upscale event with open bar and complimentary food. The flyer should communicate, a private, safe and fun event. This is PGL American Football watch party. I would like the flyer to be 650 pixels wide. It can be any length.
- Harborlight Capital Presents The 4th Annual
All-Inclusive Big Game Watch Party
2 Feb 2014 2:30pm - 7:30pm
Ultra Luxurious 3,000 sq/ft Las Vegas Penthouse 60 Stories Above the Strip
7-foot HD Projector Screen & Kelvo Sound System
Top Shelf Open Bar & Complimentary Food
PURCHASE TICKETS HERE: http://2014fieldday.ticketlark.example
PROCEEDS TO BE DONATED TO HOMEFRONT ALLIES LAS VEGAS
(Pictures of AMERICAN football players, footballs, Stadiums...etc Get creative!) American football, not soccer.
Flyer must be 650 pixels wide & it can be any length.
- Flyer Cannot Say Grand Clash,
Flyer Cannot have PGL Logo or any PGL Football Team Logos

```html
<!DOCTYPE html>
<html lang="en">
<head>
<meta charset="utf-8">
<title>Big Game Watch Party Flyer</title>
<link rel="stylesheet" href="https://fonts.googleapis.com/css2?family=Anton&family=Montserrat:wght@400;600;700;800&display=swap">
<style>
  :root {
    --night: #02060d;
    --stadium-blue: #0d3a78;
    --light-blue: #7fc4ff;
    --turf-dark: #0c3a14;
    --turf: #2f7a2a;
    --turf-light: #4f9a3c;
    --white: #ffffff;
    --silver-top: #ffffff;
    --silver-mid: #b9c2cc;
    --silver-low: #6f7a86;
    --brand-purple: #4a1f6e;
    --brand-gold: #e7c14a;
  }
  html, body {
    margin: 0;
    padding: 0;
    width: 1200px;
    height: 2584px;
    overflow: hidden;
    background: var(--night);
  }
  .flyer {
    position: relative;
    width: 1200px;
    height: 2584px;
    overflow: hidden;
    font-family: "Montserrat", sans-serif;
    color: var(--white);
    text-align: center;
  }
  .stadium-scene {
    position: absolute;
    left: 0; top: 0;
    width: 1200px; height: 1180px;
    background:
      radial-gradient(ellipse 260px 160px at 140px 470px, rgba(160,215,255,.85), rgba(40,110,200,.25) 60%, transparent 80%),
      radial-gradient(ellipse 260px 160px at 1060px 470px, rgba(160,215,255,.85), rgba(40,110,200,.25) 60%, transparent 80%),
      radial-gradient(ellipse 380px 460px at 600px 360px, #3c4a5a, #141c26 60%, transparent 85%),
      linear-gradient(180deg, var(--night) 0%, #061226 40%, var(--stadium-blue) 75%, #0a2a30 100%);
  }
  .field-scene {
    position: absolute;
    left: 0; top: 1100px;
    width: 1200px; height: 1484px;
    background: linear-gradient(180deg, #0f4a1a 0%, var(--turf) 18%, var(--turf-light) 45%, var(--turf) 75%, var(--turf-dark) 100%);
  }
  .field-lines {
    position: absolute;
    left: 0; top: 1100px;
  }
  .line {
    position: absolute;
    left: 0;
    width: 1200px;
    margin: 0;
  }
  .presenter {
    top: 60px;
    font-weight: 800;
    font-size: 50px;
    line-height: 1.12;
    letter-spacing: 1px;
    text-shadow: 0 3px 8px rgba(0,0,0,.8);
  }
  .silver {
    font-family: "Anton", sans-serif;
    text-transform: uppercase;
    background: linear-gradient(180deg, var(--silver-top) 0%, var(--silver-mid) 50%, var(--silver-low) 52%, #dfe5ea 100%);
    -webkit-background-clip: text;
    background-clip: text;
    color: transparent;
    filter: drop-shadow(0 6px 4px rgba(0,0,0,.85));
  }
  .edition { top: 628px; font-size: 40px; letter-spacing: 2px; }
  .inclusive { top: 680px; font-size: 96px; line-height: 1; }
  .big-game { top: 784px; font-size: 170px; line-height: 1; letter-spacing: 4px; }
  .watch-party { top: 964px; font-size: 64px; line-height: 1; letter-spacing: 3px; }
  .event-date {
    top: 1170px;
    font-family: "Anton", sans-serif;
    font-size: 164px;
    line-height: 1;
    letter-spacing: 4px;
    text-shadow: 0 6px 10px rgba(0,0,0,.55);
  }
  .event-time {
    top: 1370px;
    font-family: "Anton", sans-serif;
    font-size: 80px;
    line-height: 1;
    letter-spacing: 3px;
    text-shadow: 0 4px 8px rgba(0,0,0,.55);
  }
  .detail {
    font-weight: 600;
    font-size: 42px;
    letter-spacing: 1px;
    text-shadow: 0 3px 6px rgba(0,0,0,.6);
  }
  .venue-size { top: 1500px; }
  .venue-name {
    top: 1552px;
    font-family: "Anton", sans-serif;
    font-size: 96px;
    line-height: 1;
    letter-spacing: 2px;
    text-shadow: 0 4px 8px rgba(0,0,0,.55);
  }
  .venue-height { top: 1668px; }
  .screen { top: 1772px; }
  .sound { top: 1848px; }
  .hospitality {
    top: 1940px;
    font-family: "Anton", sans-serif;
    font-size: 68px;
    letter-spacing: 2px;
    text-shadow: 0 4px 8px rgba(0,0,0,.55);
  }
  .fine-print {
    position: absolute;
    left: 80px;
    width: 640px;
    text-align: left;
    font-weight: 700;
    font-size: 30px;
    line-height: 1.35;
    text-transform: uppercase;
    text-shadow: 0 2px 5px rgba(0,0,0,.6);
  }
  .tickets { top: 2236px; }
  .tickets .url { text-transform: none; font-size: 27px; }
  .charity { top: 2390px; }
  .brand {
    position: absolute;
    left: 760px;
    top: 2280px;
    width: 400px;
    display: flex;
    align-items: center;
    gap: 22px;
  }
  .brand-mark {
    width: 120px; height: 120px;
    border-radius: 50%;
    background: var(--brand-gold);
    flex: none;
  }
  .brand-name {
    font-weight: 700;
    font-size: 40px;
    line-height: 1.1;
    color: var(--white);
    text-align: left;
  }
</style>
</head>
<body>
  <main class="flyer">
    <div class="stadium-scene" role="img" aria-label="Night stadium with bright floodlights and an American football player diving with the ball"></div>
    <div class="field-scene" role="img" aria-label="Green American football field turf seen from ground level"></div>
    <svg class="field-lines" width="1200" height="1484" viewBox="0 0 1200 1484" aria-hidden="true">
      <line x1="0" y1="40" x2="1200" y2="40" stroke="#ffffff" stroke-width="6" opacity=".85"/>
      <line x1="0" y1="290" x2="1200" y2="290" stroke="#ffffff" stroke-width="5" opacity=".55"/>
      <line x1="600" y1="40" x2="600" y2="1484" stroke="#ffffff" stroke-width="8" opacity=".25"/>
    </svg>

    <p class="line presenter">HARBORLIGHT CAPITAL<br>PRESENTS</p>
    <p class="line silver edition">The 4th Annual</p>
    <p class="line silver inclusive">All Inclusive</p>
    <p class="line silver big-game">Big Game</p>
    <p class="line silver watch-party">Watch Party</p>

    <p class="line event-date">2 FEB 2014</p>
    <p class="line event-time">2:30PM - 7:30PM</p>

    <p class="line detail venue-size">ULTRA LUXURIOUS 3,000 SQ/FT</p>
    <p class="line venue-name">LAS VEGAS PENTHOUSE</p>
    <p class="line detail venue-height">60 STORIES ABOVE THE STRIP</p>
    <p class="line detail screen">7-FOOT HD PROJECTOR SCREEN</p>
    <p class="line detail sound">&amp; KELVO SOUND SYSTEM</p>
    <p class="line hospitality">OPEN BAR &amp; COMPLIMENTARY FOOD</p>

    <p class="fine-print tickets">Purchase tickets at:<br><span class="url">www.2014fieldday.ticketlark.example</span></p>
    <p class="fine-print charity">Proceeds to be donated to<br>Homefront Allies Las Vegas</p>

    <div class="brand">
      <span class="brand-mark"></span>
      <span class="brand-name">Harborlight<br>Capital</span>
    </div>
  </main>
</body>
</html>
```